Flyer for 1 day Lean Manufacturing event

I have: 2 sample flyers for the same event, a Word document with the text I would like to use, photos to include. Not all photos need to be included.

I would like a 2 (maybe 1?) page flyer I can use for marketing this and future events. Can be MS Publisher format, or other as preferred - please provide PDF also just in case.

```html
<!DOCTYPE html>
<html lang="en">
<head>
<meta charset="utf-8">
<title>One Day Lean Manufacturing Simulation – Flyer</title>
<link rel="stylesheet" href="https://fonts.googleapis.com/css2?family=Poppins:wght@400;500;600;700&family=Oswald:wght@600&display=swap">
<style>
:root{
  --blue:#3a63b4;
  --sky:#34a8e0;
  --green:#0aab4e;
  --green-soft:#9fd8ad;
  --red:#a31f24;
  --orange:#d5511f;
  --ink:#1d1d1d;
  --paper:#ffffff;
  --backdrop:#b9b9b9;
}
*{margin:0;padding:0;box-sizing:border-box}
html,body{width:1200px;height:1117px;overflow:hidden;background:var(--backdrop)}
body{font-family:"Poppins",sans-serif;color:var(--ink);position:relative}
.page{position:absolute;top:173px;width:502px;height:709px;background:var(--paper);overflow:hidden}
.page--front{left:80px}
.page--back{left:614px}
.abs{position:absolute}
.photo{background:linear-gradient(135deg,#6f7f93,#b98a63 45%,#e07a3a 70%,#4b5563)}

/* front */
.hero-art{position:absolute;left:0;top:0}
.hero-title{left:35px;top:36px;color:#fff;font-weight:700;font-size:25.5px;line-height:1.02}
.hero-sub{left:35px;top:121px;color:#fff;font-size:18px;font-weight:400;white-space:nowrap}
.intro{left:30px;top:192px;width:441px;text-align:center;font-size:10.4px;line-height:1.2}
.intro strong{font-weight:700}
.photo--session{left:34px;top:242px;width:206px;height:123px}
.takeaways{left:256px;top:242px;width:230px;height:222px;border:2.5px solid var(--green);padding:11px 12px 0 14px;background:var(--paper);z-index:2}
.takeaways h2{color:var(--blue);font-size:10.8px;line-height:1.15;font-weight:700;margin-bottom:7px}
.takeaways ul{list-style:none}
.takeaways li{position:relative;padding-left:15px;font-size:8.8px;line-height:1.2;margin-bottom:8px}
.takeaways li::before{content:"";position:absolute;left:0;top:2px;width:8px;height:8px;border-radius:50%;background:var(--red)}
.takeaways li::after{content:"";position:absolute;left:2.3px;top:3.6px;width:2.5px;height:4px;border:solid #fff;border-width:0 1.2px 1.2px 0;transform:rotate(40deg)}
.about{left:34px;top:377px;width:208px;font-size:8.9px;line-height:1.21;letter-spacing:-.1px}
.about p{margin-bottom:10px}
.about .challenge{font-weight:600;font-size:8.3px;letter-spacing:-.2px;white-space:nowrap}
.photo--facilitator{left:248px;top:468px;width:182px;height:241px;z-index:1;background:linear-gradient(180deg,#e9edf2,#c9b2a0 40%,#3b3f47 75%,#2a2d33)}
.footer-front{left:0;top:666px}
.site{left:52px;top:679px;color:#fff;font-weight:600;font-size:12.5px}

/* back */
.topbar{left:38px;top:0;width:425px;height:7px;background:var(--orange)}
.outcomes{top:32px;font-size:9.4px;line-height:1.12;list-style:none}
.outcomes li{position:relative;padding-left:10px;margin-bottom:10px}
.outcomes li::before{content:"";position:absolute;left:0;top:4px;width:3.5px;height:3.5px;border-radius:50%;background:var(--green)}
.outcomes--a{left:38px;width:205px}
.outcomes--b{left:263px;width:205px}
.back-art{position:absolute;left:0;top:290px}
.facilitator-label{left:40px;top:334px;width:190px;height:24px;background:var(--sky);color:#fff;font-weight:700;font-size:14px;text-align:center;line-height:24px}
.facilitator-bio{left:40px;top:369px;width:200px;color:#fff;font-weight:600;font-size:9px;line-height:1.27}
.facilitator-bio p{margin-bottom:10px}
.photo--workshop{left:249px;top:248px;width:253px;height:187px;clip-path:polygon(14% 0,100% 0,100% 100%,14% 100%,0 50%);background:linear-gradient(135deg,#9fb6cc,#d9793f 45%,#5a6470 75%,#3a3f47)}
.details{left:261px;top:439px;width:241px;height:145px;background:var(--green);color:#fff;text-align:center;padding-top:10px}
.details h2{font-size:23px;font-weight:700;line-height:1.1;margin-bottom:2px}
.details p{font-size:9px;font-weight:600;line-height:1.28}
.register{left:312px;top:574px;width:138px;height:25px;border-radius:13px;background:var(--red);border:2px solid var(--green-soft);color:#fff;font-weight:700;font-size:12.5px;text-align:center;line-height:21px}
.brand{left:44px;top:650px;font-weight:700;font-size:12px;color:var(--blue);line-height:1.1;width:62px}
.phone{left:112px;top:643px;display:flex;align-items:center;gap:5px;font-family:"Oswald",sans-serif;font-weight:600;font-size:21px;letter-spacing:-.3px}
.divider{left:271px;top:644px;width:1px;height:28px;background:var(--blue)}
.contacts{left:281px;top:644px;font-weight:700;font-size:11px;line-height:1.4}
.contacts div{display:flex;align-items:center;gap:5px}
.dot{width:9px;height:9px;border-radius:50%;background:var(--orange);display:inline-block}
</style>
</head>
<body>

<section class="page page--front">
  <svg class="hero-art" width="502" height="182" viewBox="0 0 502 182">
    <polygon points="0,20 288,20 248,100 288,162 0,162" fill="var(--blue)"/>
    <polygon points="288,0 306,0 262,91 306,182 288,182 244,91" fill="var(--sky)"/>
    <polygon points="270,0 280,0 236,91 280,182 270,182 226,91" fill="var(--sky)" opacity=".55"/>
    <polygon points="0,170 270,170 274,180 0,180" fill="var(--green)"/>
  </svg>
  <div class="abs photo" role="img" aria-label="Workshop participants assembling parts at a table" style="left:282px;top:0;width:220px;height:181px;clip-path:polygon(18% 0,100% 0,100% 100%,18% 100%,0 50%)"></div>
  <h1 class="abs hero-title">One Day Lean<br>Manufacturing<br>Simulation</h1>
  <p class="abs hero-sub">Powered by Lean Grid</p>

  <p class="abs intro"><strong>Start the year with a bang!</strong> Our one day Lean and TOC Simulation shows you how to integrate Lean into your process, and demonstrates how you can lead or support successful implementation.</p>

  <div class="abs photo photo--session" role="img" aria-label="Participants working together at simulation tables"></div>

  <div class="abs takeaways">
    <h2>What will be covered and what you will take away</h2>
    <ul>
      <li>How to rate your company using a <strong>Manufacturing Excellence model,</strong> and use the model to drive improvement.</li>
      <li>How to maximise productivity using the <strong>Theory of Constraints.</strong></li>
      <li>Ability to <strong>develop people</strong> into a cohesive, flexible, and empowered autonomous team to achieve a common goal of improved performance.</li>
      <li>The application of lean methodologies across manufacturing, financials, administration and the supply chain.</li>
    </ul>
  </div>

  <div class="abs about">
    <p>The Simulation uses Lean manufacturing principles to work towards perfecting manufacturing processes. An analysis of the material and information flow leads to the elimination of non-value adding activities, elevating a "typical" production environment to best practice. The immersive nature of the Simulation results in a much deeper and long lasting understanding of the principles of Lean. These principles work in companies regardless of size or sector.</p>
    <p>The Simulation recreates the manufacturing environment through the hands-on assembly of "products" at separate work stations and all participants work together to refine the process and achieve optimum output.</p>
    <p class="challenge">(Challenge: try to beat the standing record)</p>
    <p>By applying best practice techniques under practical conditions, participants will accelerate awareness and understanding that will enhance the success rate and effectiveness of your Lean program.</p>
  </div>

  <div class="abs photo--facilitator" role="img" aria-label="Portrait of the facilitator in a dark blazer"></div>

  <svg class="abs footer-front" width="502" height="43" viewBox="0 0 502 43">
    <polygon points="0,0 16,0 32,43 0,43" fill="var(--green)"/>
    <polygon points="22,0 252,0 250,43 40,43" fill="var(--red)"/>
  </svg>
  <p class="abs site">www.leanworksevents.com</p>
</section>

<section class="page page--back">
  <div class="abs topbar"></div>
  <ul class="abs outcomes outcomes--a">
    <li>Ability to list, discuss and review process issues by using basic problem solving techniques</li>
    <li>How to identify and eliminate non-value added activities.</li>
    <li>How to distinguish between push and pull systems and understand the control method of Kanban pull signals to balance supply and demand, improve lead times and reduce work-in progress.</li>
    <li>Understand why, when, and how to practice set up time reduction.</li>
    <li>Why large batch sizes are not cost effective and increase inventory, lead times, and reduce flexibility.</li>
    <li>Why consistent processes give quality results through standard work practices and procedures.</li>
  </ul>
  <ul class="abs outcomes outcomes--b">
    <li>The importance of visual performance measures in driving behaviours.</li>
    <li>How the implementation of 5S housekeeping is the cornerstone of best practice.</li>
    <li>The importance of quality at source and mistake proofing.</li>
    <li>Why preventative and autonomous maintenance is critical to overall equipment effectiveness.</li>
    <li>Understand the key best practices areas of: Leading and Managing Change, Teamwork, Set-up Reduction, Process and Material Flow, Focused Improvement, 5S, and Visual Performance Measures.</li>
  </ul>

  <svg class="back-art" width="502" height="419" viewBox="0 0 502 419">
    <rect x="0" y="8" width="263" height="10" fill="var(--green)"/>
    <polygon points="0,24 263,24 240,60 268,148 502,148 502,321 0,321" fill="var(--blue)"/>
    <polygon points="0,419 0,374 30,419" fill="var(--green)"/>
  </svg>
  <div class="abs photo photo--workshop" role="img" aria-label="Group of participants in a hands-on simulation session"></div>

  <div class="abs facilitator-label">The facilitator</div>
  <div class="abs facilitator-bio">
    <p>Daniel Harcourt is a skilled consultant, specialising in maximising profit, capacity and unlocking production efficiency.</p>
    <p>He is a professional engineer with 18 years of consulting experience in production system design, continuous improvement tools and rapid interventions.</p>
    <p>Prior to entering consulting he gained wide-ranging experience in the Australian automotive industry implementing Lean and other World Class practices across the supply chain including Parts and Accessory, Tier 1 Supply, and Vehicle Assembly Plant. He is also a specialist in Inventory Optimisation, Energy Optimisation, Excel Auditing, and the Supply Chain Operations Reference (SCOR) Model</p>
  </div>

  <div class="abs details">
    <h2>Details</h2>
    <p>Date: Friday 16th February 2024<br>Time: 8am to 5pm<br>Catering provided<br>Venue: Lakeside Grand Hotel, Harbour Room<br>12 Example Parade<br>Northbrook QLD 4000<br>Cost: $350 per person incl GST</p>
  </div>
  <div class="abs register">REGISTER HERE</div>

  <div class="abs brand">Lean Works Events</div>
  <div class="abs phone">
    <svg width="22" height="22" viewBox="0 0 22 22"><circle cx="11" cy="11" r="11" fill="var(--green)"/><path d="M7.5 5.5l2 2.3-1.2 1.6c.8 1.7 2 2.9 3.6 3.7l1.6-1.2 2.3 2-1.2 2.1c-4.4-.3-8.3-4.2-8.6-8.6z" fill="#fff"/></svg>
    <span>555-010-2030</span>
  </div>
  <div class="abs divider"></div>
  <div class="abs contacts">
    <div><span class="dot"></span>leanworksevents.com</div>
    <div><span class="dot"></span>info@leanworksevents.com</div>
  </div>
</section>

</body>
</html>
```